Dog walking/Pet Sitting company needs a brochure to hook high end apartment tenants

We are looking for a brochure design that we can bring to meetings with high-end apartment and hotel management that will explain who we are, what we do, and how we can help their tenants/guests. I would like it to reflect the same look and feel of our website, carried over to printed brochure. Wesbite is www.harborleashpetcare.com. I can provide the stock images from the website if needed. A bi-fold brochure is ideal, unless you feel the information would fit better on a tri-fold. My company colors are #5D4664 and #5BA046. I would like a more professional tone to it, rather than fun.

Target Market(s)

Demo Professional Females and Males ages 30-50 with pets

Industry/Entity Type

Pet sitting

Font styles to use
Sans Serif

Colors
6b449b
9bcb3c

Requirements
Must have
• the same look and feel as my website; explain who we are, what we do, how we can help; include services offered; Mention that we service Parsippany and surrounding towns. Mention 15 years in business.
Should not have
• do not list pricing on brochure (you can mention pricing is available on the website). No cartoonish feel.

```html
<!DOCTYPE html>
<html lang="en">
<head>
<meta charset="utf-8">
<title>Harbor Leash Pet Care – Trifold Brochure</title>
<link href="https://fonts.googleapis.com/css2?family=Open+Sans:ital,wght@0,400;0,600;0,700;1,400&display=swap" rel="stylesheet">
<style>
  :root {
    --purple: #6b449b;
    --purple-deep: #5d4664;
    --green: #5ba046;
    --green-light: #9bcb3c;
    --paper: #ffffff;
    --ink: #4a4a4a;
    --backdrop: #9c9c9c;
  }
  * { box-sizing: border-box; margin: 0; padding: 0; }
  html, body { width: 1200px; height: 2400px; overflow: hidden; }
  body {
    background: radial-gradient(ellipse at center, #b4b4b4 0%, var(--backdrop) 70%);
    font-family: "Open Sans", Arial, sans-serif;
    color: var(--ink);
    position: relative;
  }
  .sheet {
    position: absolute; left: 50px; width: 1100px; height: 850px;
    background: var(--paper);
    box-shadow: 0 14px 40px rgba(0,0,0,.28);
    display: grid; grid-template-columns: repeat(3, 1fr);
    overflow: hidden;
  }
  .sheet--outer { top: 170px; }
  .sheet--inner { top: 1380px; }
  .panel { position: relative; padding: 40px 36px; }
  .panel + .panel { border-left: 1px solid rgba(0,0,0,.05); }

  /* photo placeholders */
  .photo { position: absolute; border-radius: 50%; }
  .photo-ring { position: absolute; pointer-events: none; }

  /* About panel */
  .about-photo { left: 58px; top: 48px; width: 250px; height: 250px; border: 10px solid var(--green);
    background: linear-gradient(135deg, #7b8f6d, #c9c3b8 55%, #f0efe9); }
  .about { position: absolute; left: 40px; right: 40px; top: 360px; }
  .heading-small { font-weight: 700; color: var(--purple); font-size: 15px; display: inline-block;
    border-bottom: 2px solid var(--green); padding-bottom: 2px; margin-bottom: 12px; }
  .about p { font-size: 12.5px; line-height: 1.55; margin-bottom: 12px; font-style: italic; }

  /* Contact panel */
  .panel--contact { background: var(--purple); color: #fff; }
  .contact-title, .follow-title { font-weight: 700; font-size: 16px; display: inline-block;
    border-bottom: 2px solid var(--green-light); padding-bottom: 2px; }
  .contact-title { position: absolute; top: 150px; left: 40px; }
  .contact-list { position: absolute; top: 200px; left: 40px; list-style: none; }
  .contact-list::before { content: ""; position: absolute; left: 14px; top: 14px; bottom: 14px; width: 2px; background: var(--green-light); }
  .contact-list li { position: relative; display: flex; align-items: center; gap: 16px; height: 46px; font-size: 14px; }
  .contact-icon { width: 30px; height: 30px; border-radius: 50%; background: var(--purple);
    border: 2px solid var(--green-light); display: grid; place-items: center; flex: none; position: relative; }
  .follow-title { position: absolute; top: 430px; left: 40px; }
  .social { position: absolute; top: 475px; left: 40px; display: flex; gap: 14px; }
  .social span { width: 26px; height: 26px; border-radius: 50%; border: 1.5px solid var(--green-light); }
  .brand-stack { position: absolute; left: 0; right: 0; bottom: 110px; display: flex; justify-content: center; align-items: center; gap: 12px; }
  .brand-stack .brand-dot { width: 18px; height: 18px; border-radius: 50%; background: #fff; }
  .brand-name--light { color: #fff; font-weight: 700; font-size: 26px; }

  /* Cover panel */
  .cover-brand { position: absolute; top: 48px; left: 0; right: 0; display: flex; justify-content: center; align-items: center; gap: 12px; }
  .cover-brand .brand-dot { width: 22px; height: 22px; border-radius: 50%; border: 3px solid var(--purple); }
  .brand-name { color: var(--purple); font-weight: 700; font-size: 24px; }
  .cover-headline { position: absolute; top: 140px; left: 40px; font-weight: 700; font-size: 32px; line-height: 1.15; color: var(--purple); }
  .cover-headline .accent { color: var(--green); }
  .bell { position: absolute; right: 40px; top: 220px; }
  .cover-tagline { position: absolute; top: 282px; left: 40px; right: 30px; color: var(--green); font-weight: 700; font-size: 17px; }
  .cover-photo { left: 38px; top: 345px; width: 290px; height: 290px;
    background: linear-gradient(140deg, #efece6, #b8a48e 45%, #3d3a3c 75%, #8c8f98); }

  /* Inner sheet */
  .inner-art { position: absolute; inset: 0; }
  .services-title { position: absolute; top: 150px; left: 0; right: 0; text-align: center; color: #fff;
    font-weight: 700; font-size: 40px; letter-spacing: 1px; line-height: 1.2; text-shadow: 0 2px 6px rgba(0,0,0,.3); }
  .service-col { position: absolute; }
  .service-col--left { left: 36px; width: 300px; top: 505px; }
  .service-col--middle { left: 402px; width: 300px; top: 525px; }
  .service-col--right { left: 768px; width: 300px; top: 430px; }
  .service { margin-bottom: 22px; }
  .service-title { display: flex; align-items: center; gap: 10px; color: var(--green); font-weight: 700; font-size: 16px; margin-bottom: 6px; }
  .service-title::before { content: ""; width: 16px; height: 16px; border-radius: 50%; background: var(--purple); flex: none; }
  .service p { font-size: 12px; line-height: 1.5; }
  .bottom-band { position: absolute; left: 0; right: 0; bottom: 0; height: 26px; background: var(--purple); }
  .fold { position: absolute; top: 0; bottom: 0; width: 1px; background: rgba(0,0,0,.06); }
</style>
</head>
<body>

<!-- Outer side -->
<section class="sheet sheet--outer">
  <div class="panel panel--about">
    <div class="photo about-photo" role="img" aria-label="Photo of a smiling white dog lying on a path with its owners"></div>
    <svg class="photo-ring" style="left:48px;top:38px" width="270" height="270" viewBox="0 0 270 270" aria-hidden="true">
      <path d="M180 20 A120 120 0 0 1 230 210" fill="none" stroke="#6b449b" stroke-width="6" stroke-linecap="round"/>
    </svg>
    <div class="about">
      <h2 class="heading-small">About Us</h2>
      <p>We specialize in one-to-one personalized, quality pet care. We offer many services to cater to your needs. Whether you have dogs, cats, reptiles or rodents, we can help!</p>
      <p>Our business was born out of necessity. There were very few options for pet owners as recently as 15 years ago. We were in the same boat, working long hours and traveling often, with a new puppy at home. We never found someone we trusted enough to care for our baby, so we built the service we wished we had. Serving Parsippany and surrounding towns.</p>
    </div>
  </div>

  <div class="panel panel--contact">
    <h2 class="contact-title">Contact us</h2>
    <ul class="contact-list">
      <li><span class="contact-icon"><svg width="14" height="14" viewBox="0 0 24 24"><path d="M6.6 10.8a15 15 0 0 0 6.6 6.6l2.2-2.2a1 1 0 0 1 1-.25 11.4 11.4 0 0 0 3.6.57 1 1 0 0 1 1 1V20a1 1 0 0 1-1 1A17 17 0 0 1 3 4a1 1 0 0 1 1-1h3.5a1 1 0 0 1 1 1c0 1.25.2 2.45.57 3.57a1 1 0 0 1-.25 1z" fill="#9bcb3c"/></svg></span>201-555-0148</li>
      <li><span class="contact-icon"><svg width="14" height="14" viewBox="0 0 24 24"><rect x="3" y="6" width="18" height="12" fill="none" stroke="#9bcb3c" stroke-width="2"/><path d="M3 6l9 7 9-7" fill="none" stroke="#9bcb3c" stroke-width="2"/></svg></span>info@harborleashpetcare.com</li>
      <li><span class="contact-icon"><svg width="14" height="14" viewBox="0 0 24 24"><circle cx="12" cy="12" r="9" fill="none" stroke="#9bcb3c" stroke-width="2"/><path d="M12 7v5l3 2" fill="none" stroke="#9bcb3c" stroke-width="2"/></svg></span>Mon-Fri: 8 am - 6 pm</li>
      <li><span class="contact-icon"><svg width="14" height="14" viewBox="0 0 24 24"><circle cx="12" cy="12" r="9" fill="none" stroke="#9bcb3c" stroke-width="2"/><path d="M3 12h18M12 3c3 3 3 15 0 18M12 3c-3 3-3 15 0 18" fill="none" stroke="#9bcb3c" stroke-width="1.5"/></svg></span>www.harborleashpetcare.com</li>
    </ul>
    <h2 class="follow-title">Follow Us</h2>
    <div class="social" aria-label="Social media links"><span></span><span></span><span></span><span></span><span></span></div>
    <div class="brand-stack"><span class="brand-dot"></span><span class="brand-name--light">Harbor Leash Pet Care</span></div>
  </div>

  <div class="panel panel--cover">
    <div class="cover-brand"><span class="brand-dot"></span><span class="brand-name">Harbor Leash Pet Care</span></div>
    <h1 class="cover-headline"><span class="accent">Ring our Bell to</span><br>Schedule a<br>Meeting</h1>
    <svg class="bell" width="64" height="48" viewBox="0 0 64 48" aria-hidden="true">
      <path d="M22 38 C22 20 26 10 32 10 C38 10 42 20 42 38 Z" fill="#6b449b"/>
      <circle cx="32" cy="41" r="4" fill="#6b449b"/>
      <path d="M14 18 A14 14 0 0 0 14 36 M8 14 A20 20 0 0 0 8 40 M50 18 A14 14 0 0 1 50 36 M56 14 A20 20 0 0 1 56 40" fill="none" stroke="#5ba046" stroke-width="2.5" stroke-linecap="round"/>
    </svg>
    <p class="cover-tagline">Let Us Help You Find Your Balance</p>
    <div class="photo cover-photo" role="img" aria-label="Photo of a woman hugging a spaniel dog on a sofa"></div>
    <svg class="photo-ring" style="left:26px;top:333px" width="314" height="314" viewBox="0 0 314 314" aria-hidden="true">
      <circle cx="157" cy="157" r="147" fill="none" stroke="#6b449b" stroke-width="4"/>
      <path d="M60 50 A135 135 0 0 1 150 22" fill="none" stroke="#5ba046" stroke-width="5" stroke-linecap="round"/>
      <path d="M285 110 A135 135 0 0 1 250 250" fill="none" stroke="#5ba046" stroke-width="5" stroke-linecap="round"/>
    </svg>
  </div>
</section>

<!-- Inner side -->
<section class="sheet sheet--inner">
  <svg class="inner-art" width="1100" height="850" viewBox="0 0 1100 850">
    <defs>
      <linearGradient id="field" x1="0" y1="0" x2="0" y2="1">
        <stop offset="0" stop-color="#2f6b24"/><stop offset="1" stop-color="#4f9a34"/>
      </linearGradient>
      <clipPath id="sheetClip"><rect x="0" y="40" width="1100" height="810"/></clipPath>
    </defs>
    <g clip-path="url(#sheetClip)">
      <ellipse cx="550" cy="60" rx="575" ry="395" fill="none" stroke="#5ba046" stroke-width="8"/>
      <ellipse cx="550" cy="60" rx="560" ry="380" fill="none" stroke="#222" stroke-width="5"/>
      <g role="img" aria-label="Photo of people walking dogs on leashes across a lawn">
        <ellipse cx="550" cy="60" rx="548" ry="368" fill="url(#field)"/>
      </g>
    </g>
    <g stroke="#6b449b" stroke-width="5">
      <g role="img" aria-label="Photo of a labrador carrying a leash"><circle cx="110" cy="200" r="68" fill="#d9b06a"/></g>
      <g role="img" aria-label="Photo of a dog eating from a bowl"><circle cx="245" cy="305" r="68" fill="#e0cba3"/></g>
      <g role="img" aria-label="Photo of a cat resting on a lap"><circle cx="440" cy="360" r="68" fill="#a8a09a"/></g>
      <g role="img" aria-label="Photo of a small dog under a knitted blanket"><circle cx="630" cy="350" r="68" fill="#8b5a58"/></g>
      <g role="img" aria-label="Photo of a woman cuddling a puppy"><circle cx="875" cy="225" r="68" fill="#8c6a55"/></g>
      <g role="img" aria-label="Photo of a dog in a bow tie at a wedding"><circle cx="935" cy="85" r="62" fill="#b9c9a6"/></g>
    </g>
  </svg>
  <h2 class="services-title">PROFESSIONAL PET<br>CARE SERVICES</h2>
  <span class="fold" style="left:366px"></span><span class="fold" style="left:733px"></span>

  <div class="service-col service-col--left">
    <div class="service"><h3 class="service-title">Dog Walking</h3>
      <p>We are pleased to provide dog walking services Monday-Friday between the hours of 10:00 am and 5:00 pm.</p></div>
    <div class="service"><h3 class="service-title">Pet Sitting</h3>
      <p>We are pleased to provide pet sitting services Monday-Friday between the hours of 10:00 am and 5:00 pm.</p></div>
    <div class="service"><h3 class="service-title">Cat Sitting/Small Pet Sitting</h3>
      <p>We are happy to offer visits specific to our furry feline friends! We call this our "Kitty Harbor" service! This service may also be used for smaller household pets such as rabbits, guinea pigs, birds or rodents.</p></div>
  </div>

  <div class="service-col service-col--middle">
    <div class="service"><h3 class="service-title">Day Care &amp; Overnight Boarding</h3>
      <p>We understand that leaving your dog at home or in a kennel is not always the best option. That's why we offer leaving your dog(s) with us at our home. We accept smaller breed dogs (approximately 30lbs or less) who are fully house-broken, neutered/spayed, and socialize well with other dogs. All vaccinations must be current, including rabies, DHLP/Parvo, and Bordetella.</p></div>
  </div>

  <div class="service-col service-col--right">
    <div class="service"><h3 class="service-title">Sleepovers</h3>
      <p>Our newest option is becoming increasingly popular with pet parents who want to leave their pets home, but not alone, overnight. Now we can arrange to have a sitter stay with your pets overnight in the comfort of your home (from 10 pm to 7 am).</p></div>
    <div class="service"><h3 class="service-title">Wedding Attendant</h3>
      <p>When they are a part of your family, they should also be a part of your wedding! We can help make your wedding dreams a reality, or at least make sure your wedding dress stays white and your tux stays black!</p></div>
  </div>
  <div class="bottom-band"></div>
</section>

</body>
</html>
```